Pilates 1 on 1 Session

A double sided DL size flyer.

Features

- Harbour Physio Logo (see EPS)
- Pictures only from our photo stock (no random downloaded images).
- Text relevant to the offer we are making (see DL Text file)
- Phone Number and Email Address
- Include photos see URL www.harbourphysio.com.au and those already attached.
- Please incorporate the pilates_studio image file attached as well.

This flyer is designed to bring people in for a 1v1 pilates session with our senior physio. Those who have health insurance will not need to pay anything out of pocket as it is completely covered. After the this session they will then be able to join any one of the other 17 Small pilates groups that we run (by small we mean max of 5 people).

Prefer cool colours like the greens from our logo and perhaps some blue as well.

Cheers

Target Market(s)

Females 20 through to 60 who are interested in fitness and personal health.

Industry/Entity Type

Health

Font styles to use
Sans Serif

Colors
acd036
9bcb3c
0255a3

Requirements
Must have
• Images of pilates equipment that were provided.
Should not have
• Any pictures that have not been supplied either as part of this job or on the website.

```html
<!DOCTYPE html>
<html lang="en">
<head>
<meta charset="utf-8">
<title>Harbour Physio – One Hour Private Pilates Session</title>
<link rel="stylesheet" href="https://fonts.googleapis.com/css2?family=Oswald:wght@500;700&family=Lato:wght@700;900&display=swap">
<style>
  :root {
    --lime: #acd036;
    --leaf: #9bcb3c;
    --deep-leaf: #7fb51f;
    --ink: #1d1d1d;
    --offer-red: #e3141b;
    --paper: #ffffff;
    --stage: #ecefe8;
    --studio-dark: #3b3d42;
    --studio-mid: #8a8f97;
    --studio-light: #dfe3e8;
  }
  * { margin: 0; padding: 0; box-sizing: border-box; }
  html, body { width: 900px; height: 1200px; overflow: hidden; background: var(--stage); }
  .canvas { position: relative; width: 900px; height: 1200px; }
  .flyer {
    position: absolute; left: 166px; top: 37px; width: 567px; height: 1125px;
    background: linear-gradient(180deg, var(--paper) 55%, #f1f2ef 100%);
    overflow: hidden; box-shadow: 0 4px 18px rgba(0,0,0,.18);
  }
  .hero { position: absolute; left: 0; top: 0; width: 567px; height: 560px; }
  .brand {
    position: absolute; left: 40px; top: 58px; display: flex; align-items: center; gap: 10px;
    font-family: "Lato", sans-serif; font-weight: 700; font-size: 30px; line-height: 1;
    color: var(--deep-leaf); text-transform: lowercase;
  }
  .brand-dot { width: 26px; height: 26px; border-radius: 50%; background: var(--leaf); flex: none; }
  .offer { position: absolute; left: 27px; right: 60px; top: 512px; text-align: right; color: var(--ink); }
  .offer-title { font-family: "Oswald", sans-serif; font-weight: 700; font-size: 50px; line-height: 56px; }
  .offer-session { font-family: "Oswald", sans-serif; font-weight: 700; font-size: 33px; line-height: 40px; text-align: center; letter-spacing: .3px; }
  .offer-cover { font-family: "Oswald", sans-serif; font-weight: 500; font-size: 22px; line-height: 30px; color: var(--offer-red); text-align: center; }
  .why-pill {
    position: absolute; left: 97px; top: 662px; width: 337px; height: 55px; border-radius: 12px;
    background: linear-gradient(180deg, var(--lime), var(--deep-leaf));
    display: flex; align-items: center; justify-content: center;
    font-family: "Oswald", sans-serif; font-weight: 700; font-size: 36px; letter-spacing: -.5px;
    color: var(--paper); text-shadow: 0 2px 3px rgba(0,0,0,.45);
  }
  .why-copy {
    position: absolute; left: 32px; width: 478px; top: 734px;
    font-family: "Lato", sans-serif; font-weight: 700; font-size: 22.5px; line-height: 31px;
    color: #2b2b2b; text-align: center;
  }
  .why-copy p { margin-bottom: 15px; }
  .footer { position: absolute; left: 0; bottom: 0; width: 567px; height: 140px; }
  .contact {
    position: absolute; left: 0; width: 567px; display: flex; align-items: center; justify-content: center; gap: 10px;
    font-family: "Oswald", sans-serif; font-weight: 700; color: var(--ink);
  }
  .contact-phone { top: 1022px; font-size: 30px; left: 40px; }
  .contact-web { top: 1062px; font-size: 31px; }
  .contact-icon { width: 22px; height: 22px; flex: none; }
</style>
</head>
<body>
<div class="canvas">
  <section class="flyer">
    <svg class="hero" viewBox="0 0 567 560" aria-hidden="false">
      <defs>
        <linearGradient id="studio" x1="0" y1="0" x2="1" y2="1">
          <stop offset="0" stop-color="var(--studio-light)"/>
          <stop offset=".45" stop-color="var(--studio-mid)"/>
          <stop offset="1" stop-color="var(--studio-dark)"/>
        </linearGradient>
        <radialGradient id="logo-fade" cx="0" cy="0" r="1">
          <stop offset="0" stop-color="#fff" stop-opacity="1"/>
          <stop offset=".7" stop-color="#fff" stop-opacity=".95"/>
          <stop offset="1" stop-color="#fff" stop-opacity="0"/>
        </radialGradient>
      </defs>
      <path role="img" aria-label="Photo of the pilates studio with reformer beds, towers and exercise balls"
            d="M0 0 H567 V470 C470 440 380 470 300 455 C200 440 110 380 0 385 Z" fill="url(#studio)"/>
      <rect x="0" y="0" width="230" height="210" fill="url(#logo-fade)"/>
      <path d="M0 360 C120 345 220 420 320 445 C420 470 500 450 567 420 V480 C480 470 400 500 300 475 C200 450 110 385 0 395 Z" fill="var(--lime)"/>
      <path d="M0 395 C110 385 200 450 300 475 C400 500 480 470 567 480 V505 C470 500 390 520 290 500 C190 480 100 410 0 415 Z" fill="var(--leaf)" opacity=".85"/>
      <path d="M0 415 C100 410 190 480 290 500 C390 520 470 500 567 505 V560 H0 Z" fill="var(--paper)"/>
    </svg>

    <div class="brand"><span class="brand-dot"></span>harbour physio</div>

    <div class="offer">
      <h1 class="offer-title">One Hour</h1>
      <h2 class="offer-session">PRIVATE 1 ON 1 PILATES SESSION</h2>
      <p class="offer-cover">Covered 100% by yourprivate health insurance</p>
    </div>

    <div class="why-pill">WHY JOIN WITH US</div>

    <div class="why-copy">
      <p>If You have ever wondered about trying pilates then this is a great offer for you.</p>
      <p>One hour with a principle physio who has 25 years of experience and it will be covered 100% by your health insurance.</p>
      <p>Session lats 1hour and includes a complete physiotheraphy assessment.</p>
    </div>

    <svg class="footer" viewBox="0 0 567 140" aria-hidden="true">
      <path d="M0 22 C180 -6 390 -6 567 22 V140 H0 Z" fill="var(--leaf)"/>
      <path d="M0 22 C180 -6 390 -6 567 22" fill="none" stroke="#1f2a10" stroke-width="3"/>
      <path d="M0 30 C180 8 390 8 567 30 V140 H0 Z" fill="var(--lime)"/>
    </svg>

    <div class="contact contact-phone">
      <svg class="contact-icon" viewBox="0 0 22 22" aria-hidden="true">
        <rect x="1" y="1" width="20" height="20" rx="4" fill="#fff" stroke="#4a4a4a" stroke-width="1.5"/>
        <path d="M7 5 l2.5 0 l1 3.5 l-1.8 1.2 a9 9 0 0 0 3.6 3.6 l1.2 -1.8 l3.5 1 l0 2.5 a1.5 1.5 0 0 1 -1.5 1.5 a11 11 0 0 1 -10 -10 a1.5 1.5 0 0 1 1.5 -1.5 z" fill="var(--deep-leaf)"/>
      </svg>
      <span>(08)75550192</span>
    </div>
    <div class="contact contact-web">
      <svg class="contact-icon" viewBox="0 0 22 22" aria-hidden="true">
        <rect x="1" y="1" width="20" height="20" rx="4" fill="#fff" stroke="#4a4a4a" stroke-width="1.5"/>
        <circle cx="11" cy="11" r="6.5" fill="none" stroke="var(--deep-leaf)" stroke-width="1.6"/>
        <path d="M4.5 11 H17.5 M11 4.5 C8 8 8 14 11 17.5 M11 4.5 C14 8 14 14 11 17.5" fill="none" stroke="var(--deep-leaf)" stroke-width="1.3"/>
      </svg>
      <span>www.harbourphysio.com.au</span>
    </div>
  </section>
</div>
</body>
</html>
```